Business Card for Makeup Artist

I need a business card designed for my makeup and hair artistry business which is primarily events and weddings focused. The card needs to be sleek, simple, stylish and appealing to women. I would prefer a white background but open to suggestions also. I also love the marble background look. I have attached some example pics. It needs to be a double sided card with logo and/or design on one side and contact details in the centre of the card on the other side. NO LOGO ON BACK. Examples attached.

Target Market(s)

Females age 14-55

Industry/Entity Type

Business

Contact Information for Business Card

Nora Pelling
Principal Makeup Artist
P: 0412 903 251
E: nora@lumivamakeup.com.au
W: www.lumivamakeup.com.au

Requirements
Should not have
• No yellow, green, red or blue in the design.

```html
<!DOCTYPE html>
<html lang="en">
<head>
<meta charset="utf-8">
<title>Lumiva Makeup Artistry – Business Card</title>
<link rel="stylesheet" href="https://fonts.googleapis.com/css2?family=Roboto:wght@300;400&display=swap">
<style>
  :root {
    --backdrop: #e9e4df;
    --card: #f7f7f7;
    --ink: #5d5d5f;
    --ink-dark: #2f2f31;
    --rule: #3a3a3c;
    --shadow: rgba(60, 45, 35, 0.18);
  }
  * { margin: 0; padding: 0; box-sizing: border-box; }
  html, body {
    width: 1200px;
    height: 799px;
    overflow: hidden;
  }
  body {
    position: relative;
    background: var(--backdrop);
    font-family: "Roboto", Arial, sans-serif;
    font-weight: 300;
    color: var(--ink-dark);
  }
  .card {
    position: absolute;
    top: 283px;
    width: 445px;
    height: 248px;
    background: var(--card);
    box-shadow: 0 2px 4px var(--shadow), 0 1px 1px var(--shadow);
  }
  .card--front { left: 139px; }
  .card--back  { left: 624px; }

  .brand {
    position: absolute;
    left: 26px;
    top: 140px;
    color: var(--ink);
  }
  .brand__name {
    display: block;
    font-size: 56px;
    font-weight: 300;
    line-height: 1;
    letter-spacing: 1px;
  }
  .brand__tagline {
    display: block;
    margin-top: 4px;
    margin-left: 48px;
    font-size: 19px;
    font-weight: 300;
    letter-spacing: 1px;
    line-height: 1;
  }

  .contact {
    position: absolute;
    left: 34px;
    right: 34px;
    top: 154px;
    font-size: 10px;
    color: var(--ink-dark);
  }
  .contact__row {
    display: flex;
    justify-content: space-between;
    align-items: baseline;
  }
  .contact__name {
    font-size: 13px;
    font-weight: 300;
  }
  .contact__title { font-size: 10px; }
  .contact__rule {
    height: 1.5px;
    background: var(--rule);
    margin: 4px 0 8px;
  }
  .contact__email { text-transform: uppercase; font-size: 10.5px; }
  .contact__web { margin-top: 3px; }
</style>
</head>
<body>
  <section class="card card--front" aria-label="Card front">
    <div class="brand">
      <span class="brand__name">Lumiva</span>
      <span class="brand__tagline">MAKEUP ARTISTRY</span>
    </div>
  </section>

  <section class="card card--back" aria-label="Card back">
    <div class="contact">
      <div class="contact__row">
        <span class="contact__name">Nora Pelling</span>
        <span class="contact__title">Principal Makeup Artist</span>
      </div>
      <div class="contact__rule"></div>
      <div class="contact__row">
        <span class="contact__phone">0412 903 251</span>
        <span class="contact__email">nora@lumivamakeup.com.au</span>
      </div>
      <div class="contact__web">www.lumivamakeup.com.au</div>
    </div>
  </section>
</body>
</html>
```